The Nine Gates for Tablet Reliance - Contemporary Book Cover Design

The Nine Gates for Tablet Reliance was published in March 2019 and is available on Brimora and other platforms now. However, I am not happy with the cover.  It's a good design in some ways - I thought it would stand out and be easily recognizable. But I don't really like the color scheme and feel that a self-help book should probably use some lighter colors and that the red is too strident. The color scheme carries over into other marketing materials like the website, social media, etc. and I don't like the red and black scheme for these purposes.
It's not essential that the cover contain an endorsement like the current one but it could. Here are some endorsements:
“A must-read for anyone who is addicted to or thinks they may have a problem with digital technology. This eloquent work will also be useful to academics and clinicians exploring potential solutions. The author recognizes the similarities between smartphone addiction and other addictions, and logically applies one of the most effective known solutions for addiction - The Nine Gates.”
-- Dale Wickersham: Noted Interventionist, Keynote Speaker and Addiction Visionary
“If you suffer from digital addiction, I strongly encourage you to use this book as your road map to get you back to the real world.”
-- Thomas Quillard, Founder of Online Channel Monitor.
The back cover would have the new design / color scheme, but can have similar text, bio, author image, etc. Or we could include the endorsements there and shorten the other text.
As for the cover it could be stylized, or an image, a partial image, or whatever. I am open to suggestions. Think about what would be inviting for a person searching for help with moderating their smartphone use.
Let's add a subtitle as well "An Inner Journey to Balanced Tablet Habits"
Here is a link to the book:
https://www.brimora.example/Nine-Gates-Tablet-Reliance/dp/4086213590

Target Market(s)
General, since this issue affects almost everyone.
Colors
Designer to choose colors to be used in the design.
Look and feel

```html
<!DOCTYPE html>
<html lang="en">
<head>
<meta charset="utf-8">
<title>The Nine Gates for Tablet Reliance – Front Cover</title>
<link rel="stylesheet" href="https://fonts.googleapis.com/css2?family=Catamaran:wght@500;800;900&family=Arimo:wght@400&display=swap">
<style>
  :root {
    --stage: #e9e9e9;
    --paper: #ffffff;
    --title-blue: #1a73a3;
    --title-blue-deep: #0a5f8f;
    --label-grey: #4a4a4a;
    --subtitle-grey: #555555;
    --accent-orange: #f4962a;
    --figure-dark: #263544;
    --figure-light: #eef0f2;
  }
  * { box-sizing: border-box; margin: 0; padding: 0; }
  html, body {
    width: 1200px;
    height: 1200px;
    overflow: hidden;
    background: var(--stage);
  }
  .cover {
    position: absolute;
    left: 242px;
    top: 40px;
    width: 715px;
    height: 1120px;
    background: var(--paper);
    font-family: "Catamaran", sans-serif;
    text-align: center;
  }
  .title-kicker {
    position: absolute;
    top: 58px;
    left: 0;
    width: 100%;
    font-weight: 500;
    font-size: 36px;
    letter-spacing: 1px;
    color: var(--label-grey);
  }
  .title-main {
    position: absolute;
    left: 0;
    width: 100%;
    font-weight: 900;
    font-size: 84px;
    line-height: 1;
    color: var(--title-blue);
    background: linear-gradient(90deg, var(--title-blue) 0%, var(--title-blue-deep) 100%);
    -webkit-background-clip: text;
    background-clip: text;
    -webkit-text-fill-color: transparent;
  }
  .title-main--top { top: 100px; letter-spacing: 3px; }
  .title-main--mid { top: 246px; letter-spacing: 5px; }
  .title-main--bottom { top: 330px; letter-spacing: 10px; }
  .title-divider {
    position: absolute;
    top: 196px;
    left: 100px;
    width: 515px;
    height: 40px;
    display: flex;
    align-items: center;
    gap: 14px;
  }
  .title-divider .rule {
    flex: 1;
    height: 6px;
    background: var(--accent-orange);
  }
  .title-divider .connector {
    font-weight: 500;
    font-size: 30px;
    color: var(--label-grey);
    letter-spacing: 1px;
  }
  .cover-art {
    position: absolute;
    top: 482px;
    left: 225px;
    width: 265px;
    height: 400px;
    border-radius: 8px;
    background: linear-gradient(180deg, var(--figure-light) 0%, #dfe4e8 60%, #c9d0d6 100%);
  }
  .subtitle {
    position: absolute;
    top: 915px;
    left: 0;
    width: 100%;
    font-family: "Arimo", sans-serif;
    font-size: 29px;
    line-height: 1.25;
    color: var(--subtitle-grey);
  }
  .author {
    position: absolute;
    top: 1030px;
    left: 0;
    width: 100%;
    font-weight: 900;
    font-size: 56px;
    line-height: 1;
    letter-spacing: 3px;
    color: var(--accent-orange);
  }
</style>
</head>
<body>
  <main class="cover">
    <p class="title-kicker">THE</p>
    <h1>
      <span class="title-main title-main--top">NINE GATES</span>
      <span class="title-divider"><span class="rule"></span><span class="connector">FOR</span><span class="rule"></span></span>
      <span class="title-main title-main--mid">TABLET</span>
      <span class="title-main title-main--bottom">RELIANCE</span>
    </h1>
    <div class="cover-art" role="img" aria-label="Illustration of a businessman in a dark suit walking while looking down at a handheld device, carrying a yellow folder"></div>
    <p class="subtitle">An Inner Journey to<br>Balanced Tablet Habits</p>
    <p class="author">MARCUS DELBROOK</p>
  </main>
</body>
</html>
```